Cutting edge industrial lubricant business. Information web site. Modeled off parent web site in U

We need an informative cutting edge website to deliver information to the world about our lubrication products. Our product range includes additives and also fully formulated oils and fully formulated grease. Motor Oils, Industrial Oils, Grease. Our USA parent company has a website - see www.qorvelgroupinc.com.
Video files of our products:
https://www.vidtrelo.com/watch?v=8KbW2pLm4Qa
https://www.vidtrelo.com/watch?v=R-J7xWq_nTd
https://www.vidtrelo.com/watch?v=mb5HcYoWplZ
https://www.vidtrelo.com/watch?v=Z9wKeqf-2Ru&t=8s

Target Market(s)

Industrial customers: Truck Transport companies, Bus companies, Mining, Industrial Manufacturing

Industry/Entity Type

Business

Coding

Coded - Design and coding required

Number of Pages Required

5+ page

Font styles to use
Sans Serif

Colors
3176b5
f04a50
1b1b1b
b2b2b2
e8e8e8
acd036

Requirements
Must have
• * Information about QVG
• * Information about Bralimox (We are the exclusive distributors of all QVG products in Australia, New Zealand and Papua New Gunea)
• * Information about the products
• * Links to Data Sheets of Products
• * Video files about the products

```html
<!DOCTYPE html>
<html lang="en">
<head>
<meta charset="utf-8">
<title>Bralimox – News &amp; Newsletter</title>
<link href="https://fonts.googleapis.com/css2?family=Montserrat:wght@400;500;600&family=Open+Sans:wght@400;600&display=swap" rel="stylesheet">
<style>
:root{
  --blue:#3176b5;
  --red:#f04a50;
  --ink:#1b1b1b;
  --grey:#b2b2b2;
  --light:#e8e8e8;
  --muted:#8a8a8a;
  --footer:#212121;
  --footer-bottom:#2a2a2a;
}
*{box-sizing:border-box;margin:0;padding:0}
html,body{width:1200px;height:1200px;overflow:hidden;background:#fff}
body{position:relative;font-family:"Open Sans",Arial,sans-serif;color:var(--ink)}
.abs{position:absolute}
.eyebrow{position:absolute;left:0;width:1200px;text-align:center;font-family:"Montserrat",Arial,sans-serif;font-size:11px;letter-spacing:.3px;color:#8d8d8d;text-transform:uppercase}
.section-title{position:absolute;left:0;width:1200px;text-align:center;font-family:"Montserrat",Arial,sans-serif;font-size:26px;font-weight:500;letter-spacing:.4px;color:var(--ink);text-transform:uppercase}
.divider{position:absolute;left:507px;width:184px;height:3px}
.divider::before{content:"";position:absolute;left:0;top:0;width:33px;height:3px;border-radius:2px;background:var(--red)}
.divider::after{content:"";position:absolute;left:37px;top:0;width:147px;height:3px;border-radius:2px;background:var(--ink)}

/* news */
.news{position:absolute;top:0;left:0;width:1200px;height:475px;background:#fff}
.card{position:absolute;width:420px;height:132px}
.card-media{position:absolute;left:0;top:0;width:207px;height:132px}
.date-badge{position:absolute;left:5px;top:5px;width:36px;height:36px;background:var(--blue);color:#fff;font-size:10px;line-height:10px;text-align:center;padding-top:8px;font-family:"Open Sans",Arial,sans-serif}
.card-body{position:absolute;left:223px;top:4px;width:200px}
.card-title{font-family:"Montserrat",Arial,sans-serif;font-size:10.8px;font-weight:400;line-height:15px;color:#2a2a2a;text-transform:uppercase;white-space:nowrap;letter-spacing:-.1px}
.card-meta{position:absolute;top:36px;left:0;width:186px;height:12px;font-size:10px;color:#444;display:flex;align-items:center}
.card-meta .author{margin-left:6px}
.card-meta .shares{margin-left:auto;display:flex;gap:15px}
.card-meta .shares span{width:5px;height:5px;border-radius:50%;background:#333}
.card-text{position:absolute;top:55px;left:0;width:186px;font-size:8.6px;line-height:11.3px;color:var(--muted)}
.card-link{position:absolute;top:104px;left:-1px;font-size:12px;color:var(--red)}

/* newsletter */
.newsletter{position:absolute;top:474px;left:0;width:1200px;height:333px;background:radial-gradient(ellipse at 45% 60%,#f1f1f3 0%,#e7e7ea 55%,#dfe0e3 100%)}
.subscribe-field{position:absolute;left:363px;top:675px;width:361px;height:31px;border-bottom:1px solid #9c9c9c;font-size:12.5px;color:var(--red);padding-top:8px;letter-spacing:.2px}
.subscribe-btn{position:absolute;left:760px;top:675px;width:129px;height:31px;background:var(--blue);color:#fff;font-family:"Montserrat",Arial,sans-serif;font-weight:600;font-size:11.5px;text-align:center;line-height:31px;letter-spacing:.2px}

/* footer */
.footer{position:absolute;top:807px;left:0;width:1200px;height:335px;background:var(--footer);color:#fff}
.footer-bottom{position:absolute;top:1142px;left:0;width:1200px;height:58px;background:var(--footer-bottom);color:#e6e6e6;font-size:11px;text-align:center;line-height:58px}
.foot-head{position:absolute;top:860px;font-size:14px;font-weight:400;color:#f2f2f2}
.contact-line{position:absolute;left:174px;font-size:10px;line-height:17px;color:#f0f0f0}
.contact-icon{position:absolute;left:148px}
.link-list{position:absolute;list-style:none;font-size:10px;color:#ececec}
.link-list li{height:22.6px;position:relative;padding-left:16px}
.link-list li::before{content:"";position:absolute;left:0;top:4px;width:4px;height:4px;border-right:1px solid #9a9a9a;border-top:1px solid #9a9a9a;transform:rotate(45deg)}
.brand-name{position:absolute;font-family:"Open Sans",Arial,sans-serif;font-size:22px;color:#f0f0f0;letter-spacing:.5px}
.brand-mark{position:absolute;width:22px;height:22px;border-radius:50%;background:var(--red)}
.product-shot{position:absolute;left:938px;top:910px;width:111px;height:149px;background:linear-gradient(165deg,#1c2230 0%,#1b3f86 55%,#2f6fd0 100%)}
.foot-rule{position:absolute;left:148px;top:1081px;width:900px;height:1px;background:#3e3e3e}
.social{position:absolute;top:1096px;width:28px;height:28px;border-radius:50%}
</style>
</head>
<body>

<section class="news">
  <p class="eyebrow" style="top:31px">Lorem ipsum is simply dummy text</p>
  <h2 class="section-title" style="top:53px">Latest News</h2>
  <div class="divider" style="top:97px"></div>

  <article class="card" style="left:169px;top:131px">
    <div class="card-media" role="img" aria-label="Oil pump jacks silhouetted against a sunset sky" style="background:linear-gradient(180deg,#5c6a70 0%,#3e4135 55%,#b98a2a 85%,#2b2414 100%)"></div>
    <div class="date-badge">22<br>AUG</div>
    <div class="card-body">
      <h3 class="card-title">Lorem ipsum is simply dummy<br>text of the printing</h3>
      <div class="card-meta">
        <svg width="8" height="9" viewBox="0 0 8 9"><circle cx="4" cy="2.3" r="2.2" fill="#333"/><path d="M0 9c0-3 1.8-4.3 4-4.3S8 6 8 9z" fill="#333"/></svg>
        <span class="author">Admin</span>
        <span class="shares"><span></span><span></span><span></span></span>
      </div>
      <p class="card-text">Lorem Ipsum is simply dummy text of the printing and typesetting industry. Lorem Ipsum has been the industry's standard</p>
      <a class="card-link">Read full article...</a>
    </div>
  </article>

  <article class="card" style="left:619px;top:131px">
    <div class="card-media" role="img" aria-label="Refinery towers and pipework under a clear blue sky" style="background:linear-gradient(180deg,#4f86c9 0%,#8fb3dc 45%,#b9c0c8 70%,#6f7479 100%)"></div>
    <div class="date-badge">22<br>AUG</div>
    <div class="card-body">
      <h3 class="card-title">Lorem ipsum is simply dummy<br>text of the printing</h3>
      <div class="card-meta">
        <svg width="8" height="9" viewBox="0 0 8 9"><circle cx="4" cy="2.3" r="2.2" fill="#333"/><path d="M0 9c0-3 1.8-4.3 4-4.3S8 6 8 9z" fill="#333"/></svg>
        <span class="author">Admin</span>
        <span class="shares"><span></span><span></span><span></span></span>
      </div>
      <p class="card-text">Lorem Ipsum is simply dummy text of the printing and typesetting industry. Lorem Ipsum has been the industry's standard</p>
      <a class="card-link">Read full article...</a>
    </div>
  </article>

  <article class="card" style="left:169px;top:293px">
    <div class="card-media" role="img" aria-label="Drilling rig and valves at an oil field" style="background:linear-gradient(180deg,#3d73b8 0%,#7ea5d4 45%,#5f6e82 75%,#2c3443 100%)"></div>
    <div class="date-badge">22<br>AUG</div>
    <div class="card-body">
      <h3 class="card-title">Lorem ipsum is simply dummy<br>text of the printing</h3>
      <div class="card-meta">
        <svg width="8" height="9" viewBox="0 0 8 9"><circle cx="4" cy="2.3" r="2.2" fill="#333"/><path d="M0 9c0-3 1.8-4.3 4-4.3S8 6 8 9z" fill="#333"/></svg>
        <span class="author">Admin</span>
        <span class="shares"><span></span><span></span><span></span></span>
      </div>
      <p class="card-text">Lorem Ipsum is simply dummy text of the printing and typesetting industry. Lorem Ipsum has been the industry's standard</p>
      <a class="card-link">Read full article...</a>
    </div>
  </article>

  <article class="card" style="left:619px;top:293px">
    <div class="card-media" role="img" aria-label="Red tractor pulling a green harvest trailer in a field" style="background:linear-gradient(180deg,#3f8fd6 0%,#7fb5e3 40%,#8a3b2e 62%,#3d5a2c 100%)"></div>
    <div class="date-badge">22<br>AUG</div>
    <div class="card-body">
      <h3 class="card-title">Lorem ipsum is simply dummy<br>text of the printing</h3>
      <div class="card-meta">
        <svg width="8" height="9" viewBox="0 0 8 9"><circle cx="4" cy="2.3" r="2.2" fill="#333"/><path d="M0 9c0-3 1.8-4.3 4-4.3S8 6 8 9z" fill="#333"/></svg>
        <span class="author">Admin</span>
        <span class="shares"><span></span><span></span><span></span></span>
      </div>
      <p class="card-text">Lorem Ipsum is simply dummy text of the printing and typesetting industry. Lorem Ipsum has been the industry's standard</p>
      <a class="card-link">Read full article...</a>
    </div>
  </article>
</section>

<section class="newsletter" aria-label="Newsletter signup"></section>
<p class="eyebrow" style="top:526px;color:#6f6f6f">Lorem ipsum is simply dummy text</p>
<h2 class="section-title" style="top:548px">Subscribe to our newsletter!</h2>
<div class="divider" style="top:592px"></div>
<svg class="abs" style="left:303px;top:682px" width="21" height="16" viewBox="0 0 21 16"><rect x="1" y="1" width="19" height="14" fill="none" stroke="#f04a50" stroke-width="1.3"/><path d="M1 1l9.5 8L20 1" fill="none" stroke="#f04a50" stroke-width="1.3"/></svg>
<div class="subscribe-field">Enter your e-mail here</div>
<div class="subscribe-btn">SUBSCRIBE NOW</div>

<footer class="footer"></footer>
<h4 class="foot-head" style="left:148px">Contact Information</h4>
<h4 class="foot-head" style="left:435px">Quick Links</h4>
<h4 class="foot-head" style="left:617px">Information</h4>
<h4 class="foot-head" style="left:938px">VELORIN</h4>

<svg class="contact-icon" style="top:909px" width="14" height="19" viewBox="0 0 14 19"><path d="M7 1a6 6 0 0 0-6 6c0 4.5 6 11 6 11s6-6.5 6-11a6 6 0 0 0-6-6z" fill="none" stroke="#fff" stroke-width="1.2"/><circle cx="7" cy="7" r="2.2" fill="none" stroke="#fff" stroke-width="1.2"/></svg>
<p class="contact-line" style="top:906px">Bralimox Pty Limited Suite 114, 8 Harlow<br>Street, Corrin Junction, NSW, 2031,</p>
<svg class="contact-icon" style="top:956px" width="16" height="16" viewBox="0 0 16 16"><path d="M4 1.5l2.5 3-1.5 2c1 2 2.5 3.5 4.5 4.5l2-1.5 3 2.5-1.5 2.5C8 15 1 8 1.5 3z" fill="none" stroke="#fff" stroke-width="1.2" stroke-linejoin="round"/></svg>
<p class="contact-line" style="top:956px">Call Now: +61 2 5550 1427</p>
<svg class="contact-icon" style="top:985px" width="15" height="12" viewBox="0 0 15 12"><rect x=".7" y=".7" width="13.6" height="10.6" rx="1.5" fill="none" stroke="#fff" stroke-width="1.2"/><path d="M1 1.5l6.5 5 6.5-5" fill="none" stroke="#fff" stroke-width="1.2"/></svg>
<p class="contact-line" style="top:982px">Email:&nbsp; admin@bralimox.com.au</p>

<ul class="link-list" style="left:435px;top:906px">
  <li>About</li><li>Products</li><li>Applications</li><li>Technology</li><li>FAQ</li>
</ul>
<ul class="link-list" style="left:617px;top:906px">
  <li>Distributors</li><li>Contact Us</li><li>Privacy</li><li>NEWS</li>
</ul>

<span class="brand-mark" style="left:742px;top:914px"></span>
<span class="brand-name" style="left:772px;top:908px">bralimox</span>
<span class="brand-mark" style="left:742px;top:986px;background:#fff"></span>
<span class="brand-name" style="left:772px;top:980px">Feltrane</span>

<div class="product-shot" role="img" aria-label="Bottle label of Velorin 15W-40 heavy duty diesel engine oil"></div>

<div class="foot-rule"></div>
<a class="social" style="left:516px;background:#3b5998" aria-label="Social profile one"></a>
<a class="social" style="left:551px;background:#3fa9f5" aria-label="Social profile two"></a>
<a class="social" style="left:585px;background:#4f6f95" aria-label="Social profile three"></a>
<a class="social" style="left:620px;background:#34465d" aria-label="Social profile four"></a>
<a class="social" style="left:654px;background:#ea4c89" aria-label="Social profile five"></a>

<div class="footer-bottom">© 2017 QVG USA Corp - Maintained By Quellmark Industrial Solutions</div>

</body>
</html>
```